Designing a new homepage for www.Brindlework.net

WEBSITE: www.brindlework.net

ABOUT THE WEBSITE
The Brindlework.net (BWK) website contains a large directory of over 50,000 international trade service providers that is not valued enough on the homepage (HP). Currently from the HP, the site appears as a general site about imports and exports (international trade). As a result, it contradicts the purpose and experience of the site.
The website is new and original for international trade online: it is a tool to find the best experts and professionals that can help importers and exporters to implement their overseas operations.

Specifically:
a) An exporter who wants to sell in Italy can find on BWK: agents to distribute their products, a lawyer for reviewing contracts, translators to translate brochures and websites, an export consultant, etc. Various local providers that can help sell their products in Italy, a local provider (e.g. based in Italy) are generally more efficient and less costly than a supplier in the exporter’s home country

b) An importer who wants to buy in China will find purchasing agents who source products for third parties; logistics companies that store and ship merchandise; corporate quality control to ensure product quality before shipment, etc.; various local providers based in China to better organize its import operation.

BWK is therefore a very resourceful solution for SMEs who want to develop, improve and organize their international trade:
a) it significantly increases their ability to create new opportunities by using the services of a third party: export to a new country; import a new product
b) it allows them to optimize their purchases of services by seeking alternatives: find a less expensive carrier, a foreign lawyer challenged by a local lawyer

It is the perfect complement to cross border marketplaces (e.g. Quorvanta.com, fenwickmarts.com, zl48.com) which concentrate on the search for products (and of companies/counterparts) but:
a) help the user to import only, not really export
b) do not help implement the operations of exporting/importing from A to Z

Therefore, BWK offers a new way of “easy exporting” (or easy importing).

THE BRIEF

The objective of the project is to rethink the HP (and the site design) to highlight this experience: "export and import more successfully through 50,000+ service providers in over 100 countries”.
We have created a wireframe (see attached) of the structure we feel best meets this objective. What do you think? Do we meet it through our wireframe? Then, next step is to take this wireframe and create a clear design that really helps us to achieve our objective.

It is considered that the site captures the importers/exporters seeking to increase their exports or to better organize their imports (but we do not start from a priori that these users are looking for service providers).
The HP should highlight the importance of service providers addressing export markets or better organizing their imports; the "market analyses" of the site should act as a "knowledge resource", where the site offers more the main experience: if you want to export to a country you have any interest to first explore what the partners listed by BWK can provide.

Reason: We feel that we're seeing some interesting designs and would like to give current and even potential submissions more time. So far we have not seen the one that really strikes us, so perhaps more time is what we and the designers need! Thanks!

Target Market(s)

Importers, exporters, international trade service providers, foreign investors, etc

Industry/Entity Type

Lawyer

Requirements
Must have
• • Please use the current basic design elements of the website, including the logo, (www.brindlework.net). These include colors and fonts, etc. We only aim to change the HP and therefore, only implement a change to the header and footer of the whole site.
• Please find inspiration from our wireframes (attached), as they have been carefully thought about by our own team. However, should you feel the need to challenge the wireframes, please do so in your design, we're interested to see what you can present us.
• Our prime objective in terms of design: creating a more user-friendly interface on the HP to guide users into the rest of the website
• We already have a psd file based on the wireframes we’ve attached to the brief. If you would like this, so your job is easier (such as using same text as we have in the wireframes), let us know!

```html
<!DOCTYPE html>
<html lang="en">
<head>
<meta charset="utf-8">
<title>Brindlework.net – Homepage</title>
<link href="https://fonts.googleapis.com/css2?family=Arimo:ital,wght@0,400;0,700;1,400&family=Oswald:wght@400&display=swap" rel="stylesheet">
<style>
:root{
  --page:#ffffff;
  --panel:#d9d3c7;
  --panel-line:#c9c2b4;
  --text:#555555;
  --text-soft:#777777;
  --heading:#6a6a6a;
  --ink:#111111;
  --link:#3f8fd6;
  --btn:#2e95dd;
  --btn-light:#ece7dc;
  --rule:#a9a9a9;
  --badge:#9a9a9a;
  --foot-top:#ffffff;
  --foot-bottom:#dcd5c9;
}
*{margin:0;padding:0;box-sizing:border-box}
html,body{width:1200px;height:900px;overflow:hidden;background:var(--page);font-family:"Arimo",Arial,sans-serif;color:var(--text)}
.canvas{position:relative;width:1200px;height:900px;overflow:hidden}
.abs{position:absolute;white-space:nowrap}
a{color:inherit}

/* sidebar */
.sidebar{position:absolute;left:123px;top:0;width:284px;height:390px;background:#fff;border-left:1px solid #ddd;border-bottom:1px solid #ddd}
.service-list{list-style:none}
.service-list li{position:absolute;left:32px;font-size:13px;color:var(--text)}
.service-list li::before{content:"";position:absolute;left:-19px;top:6px;width:5px;height:5px;border-radius:50%;background:#777}
.view-all{font-size:11px;color:var(--text);text-decoration:underline}

/* main panel */
.panel{position:absolute;left:406px;top:0;width:669px;height:390px;background:var(--panel)}
.panel-rule{position:absolute;left:0;top:81px;width:669px;height:1px;background:var(--panel-line)}
.teaser{font-size:13px;font-style:italic;color:#666;line-height:15px}
.small-link{font-size:11px;color:var(--link);text-decoration:underline}
.btn-light{position:absolute;background:var(--btn-light);border:1px solid #c2baa9;font-family:"Oswald",sans-serif;font-size:12px;color:#222;display:flex;align-items:center;justify-content:center;letter-spacing:.2px}
.btn-blue{position:absolute;left:528px;top:35px;width:133px;height:38px;background:var(--btn);font-family:"Oswald",sans-serif;font-size:12px;color:#fff;display:flex;align-items:center;justify-content:center}
.promo-title{font-size:19px;font-weight:700;color:#666}
.section-title{font-size:16px;font-weight:700;color:var(--heading)}
.tip-cat{font-size:12px;color:var(--link)}
.tip-cat.dark{color:var(--ink)}
.tip-title{font-size:12px;font-weight:700;color:#555}
.tip-meta{font-size:11px;color:#666}
.tip-meta b{font-weight:400;color:var(--ink)}
.stars{font-size:13px;color:#6a8cc9;letter-spacing:1px}
.stars span{color:#ccc}
.rated{font-size:12px;color:#777}
.pdf{position:absolute;width:44px;height:26px}
.kr-intro{font-size:12px;font-weight:700;color:#555}
.kr-row{font-size:13px;font-weight:700;color:#666}
.kr-row .num{position:absolute;left:14px;color:var(--ink)}
.kr-row .label{position:absolute;left:63px}
.kr-row::before{content:"";position:absolute;left:0;top:6px;width:5px;height:5px;border-radius:50%;background:var(--link)}
.select{position:absolute;left:358px;top:271px;width:258px;height:31px;background:linear-gradient(#f3f1ec,#ddd8ce);border:1px solid #bfb8aa;font-size:13px;font-weight:700;color:#555;padding:8px 10px}
.select-arrow{position:absolute;right:6px;top:7px;width:16px;height:16px;background:#fff;border:1px solid #999}
.ok{position:absolute;left:618px;top:271px;width:36px;height:32px;background:var(--btn-light);border:1px solid #c2baa9;font-family:"Oswald",sans-serif;font-size:13px;color:#222;display:flex;align-items:center;justify-content:center}
.popular{font-size:13px;font-weight:700;color:#555}
.country{font-size:12px;color:var(--link);text-decoration:underline}

/* partners */
.partner-rule{position:absolute;left:123px;width:949px;height:1px;background:var(--rule)}
.badge{position:absolute;background:var(--badge);border-radius:3px;opacity:.75}

/* footer */
.footer{position:absolute;left:0;top:578px;width:1200px;height:322px;background:linear-gradient(var(--foot-top),var(--foot-bottom));border-top:1px solid #eee}
.foot-head{font-size:14px;font-weight:700;color:var(--text-soft)}
.foot-link{font-size:13px;color:#666}
.foot-tour{font-size:11px;color:#555;text-decoration:underline}
.social-icon{position:absolute;width:20px;height:20px;background:#8a8a8a;border-radius:2px}
.copyright{font-size:12px;color:#888}
</style>
</head>
<body>
<div class="canvas">

  <aside class="sidebar">
    <ul class="service-list">
      <li style="top:4px">Tranlation (621)</li>
      <li style="top:30px">Debt Collection (561)</li>
      <li style="top:56px">Accounting Services (519)</li>
      <li style="top:82px">Expat Services (512)</li>
      <li style="top:108px">Market Research (512)</li>
      <li style="top:134px">Debt Collection (561)</li>
      <li style="top:164px">Freight Forwarders (7843)</li>
      <li style="top:190px">Trading Companies (2489)</li>
      <li style="top:216px">Coprorate Law (975)</li>
      <li style="top:242px">Investment Promotion (817)</li>
      <li style="top:268px">Distributors (656)</li>
      <li style="top:294px">Tranlation (621)</li>
      <li style="top:320px">Debt Collection (561)</li>
    </ul>
    <a class="abs view-all" style="left:180px;top:356px">View all services</a>
  </aside>

  <section class="panel">
    <p class="abs teaser" style="left:31px;top:-7px">significantly orem ipsum dolor sit amet, consectetur<br>adipiscing elit.orem ipsum dolor sit amet”</p>
    <a class="abs small-link" style="left:31px;top:47px">See the benefits</a>
    <div class="btn-light" style="left:228px;top:34px;width:105px;height:38px">JOIN FOR FREE</div>

    <div class="abs promo-title" style="left:449px;top:5px">brindlework.net!</div>
    <a class="abs small-link" style="left:367px;top:64px">See the benefits</a>
    <div class="btn-blue">LIST YOUR SERVICES</div>

    <div class="panel-rule"></div>

    <h2 class="abs section-title" style="left:89px;top:101px">Business Tips By Experts</h2>

    <div class="abs tip-cat" style="left:30px;top:131px">Business administration</div>
    <div class="abs tip-title" style="left:31px;top:145px">Lorem ipsum dolor sit amet, consectetur</div>
    <div class="abs tip-meta" style="left:32px;top:159px"><b>a law update</b> by Lorem Ipsum</div>
    <div class="abs stars" style="left:172px;top:177px">★★★<span>★</span></div>
    <div class="abs rated" style="left:248px;top:179px">Rated</div>

    <div class="abs tip-cat" style="left:30px;top:205px">Business administration</div>
    <div class="abs tip-title" style="left:31px;top:219px">Lorem ipsum dolor sit amet, consectetur</div>
    <div class="abs tip-meta" style="left:32px;top:233px"><b>a law update</b> by Lorem Ipsum</div>
    <div class="abs stars" style="left:172px;top:251px">★★★<span>★</span></div>
    <div class="abs rated" style="left:248px;top:253px">Rated</div>

    <div class="abs tip-cat dark" style="left:30px;top:282px">Business administration</div>
    <div class="abs tip-title" style="left:31px;top:296px">Lorem ipsum dolor sit amet, consectetur</div>
    <div class="abs tip-meta" style="left:32px;top:310px"><b>a law update</b> by Lorem Ipsum</div>
    <div class="abs stars" style="left:172px;top:328px">★★★<span>★</span></div>
    <div class="abs rated" style="left:248px;top:330px">Rated</div>

    <svg class="pdf" style="left:285px;top:171px" viewBox="0 0 44 26" aria-hidden="true"><rect x="18" y="1" width="20" height="24" fill="#fff" stroke="#777"/><rect x="1" y="6" width="28" height="13" rx="2" fill="#5b86c4"/><text x="15" y="16" font-size="9" fill="#fff" text-anchor="middle" font-family="Arimo,sans-serif">PDF</text></svg>
    <svg class="pdf" style="left:285px;top:245px" viewBox="0 0 44 26" aria-hidden="true"><rect x="18" y="1" width="20" height="24" fill="#fff" stroke="#777"/><rect x="1" y="6" width="28" height="13" rx="2" fill="#5b86c4"/><text x="15" y="16" font-size="9" fill="#fff" text-anchor="middle" font-family="Arimo,sans-serif">PDF</text></svg>
    <svg class="pdf" style="left:285px;top:322px" viewBox="0 0 44 26" aria-hidden="true"><rect x="18" y="1" width="20" height="24" fill="#fff" stroke="#777"/><rect x="1" y="6" width="28" height="13" rx="2" fill="#5b86c4"/><text x="15" y="16" font-size="9" fill="#fff" text-anchor="middle" font-family="Arimo,sans-serif">PDF</text></svg>

    <a class="abs small-link" style="left:32px;top:369px">Browse all content</a>
    <div class="btn-light" style="left:230px;top:357px;width:98px;height:28px">RECEIVE UPDATES</div>

    <h2 class="abs section-title" style="left:399px;top:98px">Knowledge Resource</h2>
    <p class="abs kr-intro" style="left:355px;top:138px">Find resources for your business amongst:</p>
    <div class="abs kr-row" style="left:362px;top:168px;width:260px"><span class="num">10,145</span><span class="label">market analyses</span></div>
    <div class="abs kr-row" style="left:362px;top:189px;width:260px"><span class="num">9,254</span><span class="label">business tips</span></div>
    <div class="abs kr-row" style="left:362px;top:209px;width:260px"><span class="num">3,215</span><span class="label">agents and distributors</span></div>
    <div class="abs kr-row" style="left:362px;top:229px;width:260px"><span class="num">50,145</span><span class="label">service providers</span></div>

    <div class="select">Select a Country<span class="select-arrow"><svg width="14" height="14" viewBox="0 0 14 14" aria-hidden="true"><path d="M3 5h8l-4 5z" fill="#555"/></svg></span></div>
    <div class="ok">OK</div>

    <div class="abs popular" style="left:358px;top:308px">Most popular:</div>
    <div class="abs country" style="left:358px;top:327px;word-spacing:8px">China, Brazil, Japan, India, Egypt, Korea, Angola,</div>
    <div class="abs country" style="left:357px;top:347px;word-spacing:8px">Italy, Englad, Romania, Spain, Argentina, France,</div>
    <div class="abs country" style="left:358px;top:367px;word-spacing:8px">China, Brazil, Japan, India, Egypt, Korea, Angola,</div>
  </section>

  <div class="partner-rule" style="top:423px"></div>
  <div class="badge" style="left:134px;top:450px;width:62px;height:62px"></div>
  <div class="badge" style="left:228px;top:446px;width:92px;height:74px;opacity:.35"></div>
  <div class="badge" style="left:360px;top:468px;width:160px;height:32px"></div>
  <div class="badge" style="left:570px;top:460px;width:118px;height:46px"></div>
  <div class="badge" style="left:736px;top:466px;width:137px;height:34px"></div>
  <div class="badge" style="left:911px;top:458px;width:155px;height:48px"></div>
  <div class="partner-rule" style="top:539px"></div>

  <footer class="footer">
    <h3 class="abs foot-head" style="left:141px;top:27px">About</h3>
    <a class="abs foot-link" style="left:141px;top:53px">About Us</a>
    <a class="abs foot-link" style="left:141px;top:76px">Partners</a>
    <a class="abs foot-link" style="left:141px;top:99px">Site Map</a>
    <a class="abs foot-link" style="left:141px;top:122px">Contact Us</a>
    <a class="abs foot-link" style="left:141px;top:145px">Terms &amp; Conditions</a>
    <a class="abs foot-link" style="left:141px;top:168px">Privacy Policy</a>

    <h3 class="abs foot-head" style="left:313px;top:27px">Most Popular pages</h3>
    <a class="abs foot-link" style="left:313px;top:53px">Distributors</a>
    <a class="abs foot-link" style="left:313px;top:76px">Country Risk</a>
    <a class="abs foot-link" style="left:313px;top:99px">Tax Law</a>
    <a class="abs foot-link" style="left:313px;top:122px">Market Research</a>
    <a class="abs foot-link" style="left:313px;top:145px">Business Develepment</a>
    <a class="abs foot-link" style="left:313px;top:168px">Mergers and Acqisitions</a>
    <a class="abs foot-link" style="left:313px;top:191px">Corporate Law</a>
    <a class="abs foot-tour" style="left:314px;top:216px">View all</a>

    <h3 class="abs foot-head" style="left:517px;top:27px">For Importers / Exporters</h3>
    <a class="abs foot-link" style="left:516px;top:53px">Import Export Services</a>
    <a class="abs foot-link" style="left:516px;top:76px">Trade Companies, Agents</a>
    <a class="abs foot-link" style="left:516px;top:99px">Market Analyses Worldwide</a>
    <a class="abs foot-link" style="left:516px;top:122px">International Business Tips</a>
    <a class="abs foot-link" style="left:516px;top:145px">Receive Offers for Services</a>
    <a class="abs foot-tour" style="left:516px;top:171px">Take a tour</a>

    <h3 class="abs foot-head" style="left:744px;top:27px">For Service Providers</h3>
    <a class="abs foot-link" style="left:742px;top:53px">Import Export Services</a>
    <a class="abs foot-link" style="left:742px;top:76px">Trade Companies, Agents</a>
    <a class="abs foot-link" style="left:742px;top:99px">Market Analyses Worldwide</a>
    <a class="abs foot-link" style="left:742px;top:122px">International Business Tips</a>
    <a class="abs foot-link" style="left:742px;top:145px">Receive Offers for Services</a>
    <a class="abs foot-tour" style="left:743px;top:169px">Take a tour</a>

    <h3 class="abs foot-head" style="left:965px;top:27px">Follow Us</h3>
    <span class="social-icon" style="left:963px;top:54px"></span><a class="abs foot-link" style="left:994px;top:57px">Newsletter</a>
    <span class="social-icon" style="left:963px;top:83px"></span><a class="abs foot-link" style="left:994px;top:86px">Chirrup</a>
    <span class="social-icon" style="left:963px;top:112px"></span><a class="abs foot-link" style="left:994px;top:115px">RSS</a>
    <h3 class="abs foot-head" style="left:965px;top:148px">Join Us</h3>
    <span class="social-icon" style="left:963px;top:177px"></span><a class="abs foot-link" style="left:994px;top:180px">Friendwall</a>
    <span class="social-icon" style="left:963px;top:207px"></span><a class="abs foot-link" style="left:994px;top:210px">Workweave</a>

    <p class="abs copyright" style="left:322px;top:263px">Brindlework.net - International Trade Resources, Import Export Services © 2012 All Rights Reserved</p>
  </footer>

</div>
</body>
</html>
```